New website for Pollard Law Firm at www.keepwinning-example.com

We are a professional law firm located in the Nashville, Tennessee USA area. We focus on personal injury law. We are looking for a slick new website that is user friendly for updating with new blogs, videos, etc. The primary colors should be red, black, and white. It should load extremely fast and have a good mobile component. The pages for the design will include a home page, about us, news, contact us, and practice page. The practice page will be copied for all the practice areas including motor vehicle accidents, slip and fall accidents, dog bites, etc. We have included an image which we would like to include in the new site which shows the color scheme The image is called banner-Car Wreck. The new website should NOT have gavels, court houses, law books, scales or the typical images for a law firm.

Target Market(s)

People in Tennessee involved in accidents

Industry/Entity Type

Legal services, law firm

Coding

Coded - Design and coding required

Number of Pages Required

5+ page

Font styles to use
Serif

Colors
EB3D1F
EC4F4E
F09395
F8D3D4
FCEDEE

Requirements
Should not have
• Gavels, columns, scales, law related images

```html
<!DOCTYPE html>
<html lang="en">
<head>
<meta charset="utf-8">
<title>Pollard Law Firm PLLC – Home</title>
<link rel="stylesheet" href="https://fonts.googleapis.com/css2?family=Cinzel:wght@400;600&family=Montserrat:wght@400;500;600;700&display=swap">
<style>
:root{
  --red:#c41f2b;
  --red-deep:#a3161f;
  --red-soft:#ec4f4e;
  --pink:#f8d3d4;
  --blush:#fcedee;
  --navy:#0e1624;
  --ink:#111318;
  --text:#3b3d44;
  --white:#ffffff;
  --serif:'Cinzel', serif;
  --sans:'Montserrat', sans-serif;
}
*{box-sizing:border-box;margin:0;padding:0}
html,body{width:1200px;height:2887px;overflow:hidden}
body{background:var(--white);font-family:var(--sans);color:var(--text)}
.page{width:1200px;height:2887px;position:relative}
.eyebrow{font-family:var(--sans);font-weight:700;font-size:11px;letter-spacing:3px;color:var(--red)}
.section-title{font-family:var(--serif);font-weight:400;color:var(--ink);letter-spacing:7px}
.lead{font-size:13px;line-height:1.6;color:var(--text)}
.btn{display:inline-block;font-family:var(--sans);font-weight:700;font-size:10px;letter-spacing:1.5px;text-transform:uppercase;padding:12px 26px;border-radius:2px}
.btn-dark{background:var(--ink);color:var(--white)}
.btn-red{background:var(--red);color:var(--white)}
.btn-outline{border:1.5px solid var(--red);color:var(--ink);background:var(--white)}
.btn-outline-light{border:1.5px solid var(--red);color:var(--white)}
.btn-white{background:var(--white);color:var(--ink)}

/* top bar */
.topbar{height:40px;background:var(--navy);color:var(--white);display:flex;justify-content:space-between;align-items:center;padding:0 125px;font-size:11px;letter-spacing:.5px}
.topbar b{font-weight:700;margin-right:8px}

/* hero */
.hero{height:600px;position:relative;overflow:hidden}
.hero-photo{position:absolute;inset:0;background:
  linear-gradient(180deg,rgba(10,16,28,.92) 0%,rgba(22,28,44,.75) 30%,rgba(120,70,40,.55) 58%,rgba(40,24,18,.9) 80%,#120c0a 100%),
  linear-gradient(90deg,#1a2030 0%,#6b4a32 55%,#c98a4a 100%)}
.site-header{position:absolute;top:28px;left:125px;right:125px;display:flex;align-items:center;justify-content:space-between}
.brand{font-family:var(--serif);font-weight:400;color:var(--red-soft);line-height:1.05;letter-spacing:1px}
.brand .line1{font-size:28px;display:block}
.brand .line2{font-size:13px;display:block;letter-spacing:2px}
.nav{display:flex;align-items:center;gap:34px;font-size:10px;font-weight:700;letter-spacing:1px;color:var(--white)}
.nav .active{position:relative}
.nav .active::after{content:"";position:absolute;left:0;right:0;bottom:-8px;height:2px;background:var(--red)}
.nav .btn{margin-left:20px;padding:11px 22px}
.hero-copy{position:absolute;left:125px;top:215px;width:620px;color:var(--white)}
.hero-copy h1{font-family:var(--serif);font-weight:400;font-size:46px;line-height:1.02;letter-spacing:8px}
.hero-copy p{font-size:13px;line-height:1.6;margin:22px 0 30px;width:520px;color:#e8e3e0}
.hero-rail{position:absolute;left:40px;top:260px;width:1px;height:170px;background:rgba(255,255,255,.45)}
.hero-rail::after{content:"";position:absolute;left:-4px;top:180px;width:9px;height:14px;border:1px solid rgba(255,255,255,.6);border-radius:5px}
.stats{position:absolute;right:0;bottom:0;width:660px;height:155px;background:rgba(196,31,43,.86);border-bottom-right-radius:40px;display:flex;align-items:center}
.stat{flex:1;text-align:center;color:var(--white);border-right:1px solid rgba(255,255,255,.35);padding:12px 0}
.stat:last-child{border-right:0}
.stat strong{display:block;font-family:var(--sans);font-weight:600;font-size:40px;letter-spacing:1px}
.stat span{display:block;margin-top:10px;font-size:10px;font-weight:700;letter-spacing:3px}

/* about */
.about{height:300px;display:flex;align-items:center;padding:0 125px}
.about-title{width:360px}
.about-title h2{font-size:42px;line-height:1.02;margin-top:10px}
.about-divider{width:2px;height:220px;background:var(--red);margin:0 60px 0 20px}
.about-body{width:450px}
.about-body p{font-size:12px;line-height:1.6;margin-bottom:26px}

/* practice */
.practice{height:500px;background:var(--blush);position:relative;text-align:center;padding-top:70px}
.practice::before{content:"";position:absolute;left:0;top:0;bottom:0;width:18px;background:var(--red)}
.practice h2{font-size:40px}
.section-sub{width:620px;margin:18px auto 0;font-size:12px;line-height:1.6}
.cards{display:flex;justify-content:center;gap:18px;margin:40px 0 44px}
.card{width:300px;height:220px;background:var(--white);display:flex;flex-direction:column;align-items:center;justify-content:center;box-shadow:0 4px 18px rgba(0,0,0,.05)}
.card .icon{width:96px;height:96px;border-radius:50%;background:var(--blush);margin-bottom:18px}
.card h3{font-family:var(--sans);font-weight:700;font-size:14px;line-height:1.15;color:var(--ink);letter-spacing:.5px}
.card.featured{background:var(--red)}
.card.featured .icon{background:rgba(255,255,255,.22)}
.card.featured h3{color:var(--white)}

/* news */
.news{height:520px;text-align:center;padding-top:60px}
.news h2{font-size:40px}
.news-grid{display:flex;justify-content:center;gap:80px;margin-top:46px;text-align:left}
.feature{width:440px;height:300px;position:relative}
.feature .photo{position:absolute;inset:0;background:linear-gradient(135deg,#2a4f6e 0%,#8aa3b6 45%,#d9d2c6 70%,#24394e 100%)}
.caption{position:absolute;left:22px;right:22px;bottom:26px;background:var(--white);padding:20px 24px}
.caption p,.item p{font-size:11px;font-weight:600;letter-spacing:2px;color:var(--ink);line-height:1.7;text-transform:uppercase}
.rule{display:block;width:70px;height:1px;background:var(--red);margin-top:14px}
.side{width:430px;display:flex;flex-direction:column;gap:24px}
.item{display:flex;gap:34px;align-items:flex-start}
.item .thumb{width:170px;height:110px;flex:none}
.thumb-a{background:linear-gradient(135deg,#a7b4bf 0%,#7f8a93 50%,#c73a3a 100%)}
.thumb-b{background:linear-gradient(135deg,#d7dce2 0%,#5d738b 55%,#b9c4cf 100%)}
.item .rule{background:#bbb}
.side .btn{align-self:flex-start;margin-left:0;padding:13px 30px}

/* testimonial */
.testimonial{height:290px;background:var(--blush);display:flex;align-items:center;padding:0 125px}
.testimonial-title{width:430px}
.testimonial-title h2{font-size:40px;line-height:1.05;margin-top:8px}
.testimonial-divider{width:2px;height:200px;background:var(--red);margin:0 60px 0 30px}
.quote{width:420px}
.quote-mark{font-family:var(--serif);font-size:64px;line-height:.6;color:var(--red-soft);opacity:.6}
.quote p{font-size:12px;line-height:1.6;margin:12px 0 18px}
.author{display:flex;align-items:center;gap:14px}
.avatar{width:40px;height:40px;border-radius:50%;background:linear-gradient(135deg,#d9b39a,#8a5a48)}
.author span{font-size:10px;font-weight:700;letter-spacing:2px;color:var(--red)}
.arrows{margin-left:auto;display:flex;gap:4px}
.arrows svg{display:block}

/* experience */
.experience{height:320px;position:relative;background:#0b0b0d;overflow:hidden}
.experience-photo{position:absolute;left:0;top:0;width:70%;height:100%;background:radial-gradient(ellipse at 30% 55%,#8d1b22 0%,#4a0d12 40%,#120708 75%,#0b0b0d 100%)}
.experience-box{position:absolute;right:125px;top:60px;width:570px;height:200px;background:rgba(150,22,30,.82);text-align:center;color:var(--white);padding:28px 40px}
.experience-box h2{font-family:var(--serif);font-weight:400;font-size:22px;letter-spacing:5px;line-height:1.35}
.experience-box p{font-size:11px;line-height:1.6;margin:12px auto 16px;width:400px}
.experience-box .btn{padding:11px 22px}

/* footer */
.site-footer{height:277px;background:var(--red);color:var(--white);padding:44px 125px 0;position:relative}
.footer-cols{display:flex}
.footer-brand{width:470px}
.footer-brand .brand{color:var(--white)}
.footer-brand p{font-size:11px;line-height:1.6;margin-top:16px;width:340px}
.footer-col h4{font-size:10px;font-weight:700;letter-spacing:1.5px;margin-bottom:16px}
.footer-links{width:220px}
.footer-links li{list-style:none;font-size:9px;font-weight:600;letter-spacing:.5px;margin-bottom:12px}
.contact-row{display:flex;align-items:center;gap:14px;font-size:10px;margin-bottom:14px}
.contact-row .ic{width:28px;height:28px;border-radius:50%;background:var(--white);display:flex;align-items:center;justify-content:center;flex:none}
.social{position:absolute;left:0;right:0;bottom:26px;display:flex;justify-content:center;gap:12px}
.social span{width:14px;height:14px;border-radius:50%;background:var(--white);display:block}
.copyright{height:40px;background:var(--navy);color:var(--white);font-size:10px;display:flex;align-items:center;justify-content:center;letter-spacing:.5px}
</style>
</head>
<body>
<div class="page">

  <div class="topbar">
    <div><b>CALL US:</b>(615) 555-0142</div>
    <div><b>EMAIL:</b>office@pollardlaw-example.com</div>
  </div>

  <section class="hero">
    <div class="hero-photo" role="img" aria-label="City skyline at sunset by the river"></div>
    <header class="site-header">
      <div class="brand"><span class="line1">POLLARD</span><span class="line2">LAW FIRM PLLC</span></div>
      <nav class="nav">
        <span class="active">HOME</span><span>ABOUT US</span><span>NEWS</span><span>PRACTICE AREAS</span>
        <span class="btn btn-red">Contact Us</span>
      </nav>
    </header>
    <div class="hero-rail"></div>
    <div class="hero-copy">
      <h1>DON'T LOSE WHAT'S<br>LEGALLY YOURS</h1>
      <p>Lorem Ipsum is simply dummy text of the printing and typesetting industry. Lorem Ipsum has been the industry's standard dummy text ever since the 1500s</p>
      <span class="btn btn-outline-light">Contact Us</span>
    </div>
    <div class="stats">
      <div class="stat"><strong>9874</strong><span>HAPPY CLIENTS</span></div>
      <div class="stat"><strong>3584</strong><span>PROJECTS DONE</span></div>
      <div class="stat"><strong>2584</strong><span>CASE DISMISSED</span></div>
    </div>
  </section>

  <section class="about">
    <div class="about-title">
      <div class="eyebrow">ABOUT</div>
      <h2 class="section-title">POLLARD<br>LAW FIRM<br>PLLC</h2>
    </div>
    <div class="about-divider"></div>
    <div class="about-body">
      <p>WE ARE TRIAL LAWYERS AND WE ARE PROUD OF IT! There are many law firms in Tennessee who claim to be trial lawyers, but their attorneys have never seen a courtroom. We have tried hundreds of cases to verdict and we have helped thousands of people in the Tennessee courts. We fight against billion dollar insurance companies, billion dollar corporations, and the State of Tennessee, and we win!</p>
      <span class="btn btn-dark">Read More</span>
    </div>
  </section>

  <section class="practice">
    <h2 class="section-title">AREAS OF PRACTICE</h2>
    <p class="section-sub">Lorem Ipsum is simply dummy text of the printing and typesetting industry. Lorem Ipsum has been the industry's standard dummy text ever since the 1500s</p>
    <div class="cards">
      <div class="card"><div class="icon" role="img" aria-label="Motor vehicle accident icon"></div><h3>MOTOR VEHECLE<br>ACCIDENTS</h3></div>
      <div class="card featured"><div class="icon" role="img" aria-label="Slip and fall icon"></div><h3>SLIP AND FALL<br>ACCIDENTS</h3></div>
      <div class="card"><div class="icon" role="img" aria-label="Dog bite icon"></div><h3>DOG BITES</h3></div>
    </div>
    <span class="btn btn-outline">Explore More</span>
  </section>

  <section class="news">
    <h2 class="section-title">OUR LATEST NEWS</h2>
    <p class="section-sub">Lorem Ipsum is simply dummy text of the printing and typesetting industry. Lorem Ipsum has been the industry's standard dummy text ever since the 1500s</p>
    <div class="news-grid">
      <article class="feature">
        <div class="photo" role="img" aria-label="Client and lawyer reviewing documents on a tablet"></div>
        <div class="caption"><p>Lorem ipsum is simply dummy<br>text of the printing.</p><span class="rule"></span></div>
      </article>
      <div class="side">
        <article class="item">
          <div class="thumb thumb-a" role="img" aria-label="Roadside accident with warning triangle"></div>
          <div><p>Lorem ipsum is simply<br>dummy text of the<br>printing.</p><span class="rule"></span></div>
        </article>
        <article class="item">
          <div class="thumb thumb-b" role="img" aria-label="Person signing insurance paperwork"></div>
          <div><p>Lorem ipsum is simply<br>dummy text of the<br>printing.</p><span class="rule"></span></div>
        </article>
        <span class="btn btn-red">Contact Us</span>
      </div>
    </div>
  </section>

  <section class="testimonial">
    <div class="testimonial-title">
      <div class="eyebrow">WHAT</div>
      <h2 class="section-title">OUR CLIENT<br>SAY ABOUT US</h2>
    </div>
    <div class="testimonial-divider"></div>
    <div class="quote">
      <div class="quote-mark">&ldquo;&ldquo;</div>
      <p>"Speak up for those who cannot speak for themselves, for the rights of all who are destitute. Speak up and judge fairly; defend the rights of the poor and needy."</p>
      <div class="author">
        <div class="avatar" role="img" aria-label="Client portrait"></div>
        <span>M. ELLIS</span>
        <div class="arrows">
          <svg width="18" height="18" viewBox="0 0 18 18"><rect width="18" height="18" fill="#c41f2b"/><path d="M11 4 6 9l5 5" stroke="#fff" stroke-width="2" fill="none"/></svg>
          <svg width="18" height="18" viewBox="0 0 18 18"><rect width="18" height="18" fill="#c41f2b"/><path d="M7 4l5 5-5 5" stroke="#fff" stroke-width="2" fill="none"/></svg>
        </div>
      </div>
    </div>
  </section>

  <section class="experience">
    <div class="experience-photo" role="img" aria-label="Red car damaged in a collision"></div>
    <div class="experience-box">
      <h2>20 YEARS OF EXPERIENCE<br>IN VARIOUS CASES</h2>
      <p>The Pollard Law Firm began in 2005 when Mr. Pollard graduated from law school and wanted nothing more than to become a trial lawyer.</p>
      <span class="btn btn-white">Book Consultation</span>
    </div>
  </section>

  <footer class="site-footer">
    <div class="footer-cols">
      <div class="footer-brand">
        <div class="brand"><span class="line1">POLLARD</span><span class="line2">LAW FIRM PLLC</span></div>
        <p>If you are dealing with a loss caused by someone else, you do not deserve the headache and heartache involved. You should not lose what is legally yours and you need an attorney to make sure that does not happen.</p>
      </div>
      <div class="footer-col footer-links">
        <h4>QUICK LINKS</h4>
        <ul><li>HOME</li><li>ABOUT US</li><li>NEWS</li><li>PRACTICE AREAS</li><li>TESTIMONIALS</li></ul>
      </div>
      <div class="footer-col">
        <h4>CONTACT US</h4>
        <div class="contact-row"><span class="ic"><svg width="14" height="14" viewBox="0 0 24 24"><path d="M6.6 10.8a15 15 0 0 0 6.6 6.6l2.2-2.2a1 1 0 0 1 1-.25 11.4 11.4 0 0 0 3.6.57 1 1 0 0 1 1 1V20a1 1 0 0 1-1 1A17 17 0 0 1 3 4a1 1 0 0 1 1-1h3.5a1 1 0 0 1 1 1c0 1.25.2 2.45.57 3.57a1 1 0 0 1-.25 1z" fill="#111318"/></svg></span>(615) 555-0142</div>
        <div class="contact-row"><span class="ic"><svg width="14" height="14" viewBox="0 0 24 24"><rect x="3" y="5" width="18" height="14" rx="1" fill="#111318"/><path d="M3 6l9 7 9-7" stroke="#fff" stroke-width="1.6" fill="none"/></svg></span>office@pollardlaw-example.com</div>
        <div class="contact-row"><span class="ic"><svg width="14" height="14" viewBox="0 0 24 24"><path d="M12 2a7 7 0 0 0-7 7c0 5 7 13 7 13s7-8 7-13a7 7 0 0 0-7-7zm0 9.5A2.5 2.5 0 1 1 12 6.5a2.5 2.5 0 0 1 0 5z" fill="#111318"/></svg></span>1200 Maple Ridge Drive | Suite 300 |<br>Franklin, TN</div>
      </div>
    </div>
    <div class="social" aria-label="Social media links"><span></span><span></span><span></span><span></span></div>
  </footer>
  <div class="copyright">©2021 Pollard Law Firm, PLLC. All Rights Reserved.</div>

</div>
</body>
</html>
```